Up to the Challenge? Canadian based consulting company needs a two sided business card design

A Canadian based security risk management consulting company needs a two-sided business card design. What we do is provide advice and guidance related to emergency, security and business continuity management for small, medium and large companies to help ensure the protection of their people, assets, information, services, operations and reputation.

The final design should be simple, only one or two colours, eye catching, professional and one that makes people look at three or more times just because it looks so darn good.

I have include examples of business cards I like.

Target Market(s)

Small, medium and large companies.

Industry/Entity Type

Security

Contact Information for Business Card

Business Card Size: Standard size of 3.5" (89mm) x 2.0" (51mm) - (see full specifications and guides on PRINTLY's website if required)
Card Stock: Looking to use PRINTLY's Velm 32pt stock textured paper - seam colour either chili red or black
Business Name: The Harrowgate Partners
Website: www.theharrowgatepartners.example
Telephone: (555)310-2968
Name: Dana Ostrander
Position: Principle
e-mail: Dana.Ostrander@theharrowgatepartners.example

Font styles to use
Serif

Colors
ec1f27
000000
9d9d9d
aaaaaa
606060

Requirements
Must have
• - "The Harrowgate Partners" logo (see uploaded files). I have included grey scale and colour versions.
• - Business card details (as above)
Nice to have
• - One side black or grey scale.
• - Other side would likely be white.
• - Everyone likes the silver logo on the black background.
• - Small element of colour i.e. red but I'm leaning more to greyscale.
Should not have
• - A lot of colour. Keep it simple.

```html
<!DOCTYPE html>
<html lang="en">
<head>
<meta charset="utf-8">
<title>The Harrowgate Partners — Business Card</title>
<link rel="stylesheet" href="https://fonts.googleapis.com/css2?family=Cinzel:wght@400;700&family=Open+Sans:wght@400&display=swap">
<style>
  :root {
    --red: #ec1f27;
    --black: #000000;
    --card-black: #141414;
    --grey-light: #aaaaaa;
    --grey-mid: #9d9d9d;
    --grey-dark: #606060;
    --backdrop: #34302e;
    --white: #ffffff;
  }
  * { margin: 0; padding: 0; box-sizing: border-box; }
  html, body {
    width: 1200px; height: 844px; overflow: hidden;
    background: var(--backdrop);
  }
  .stage {
    width: 1200px; height: 844px;
    display: flex; align-items: center; justify-content: center; gap: 40px;
  }
  .card {
    width: 540px; height: 309px; position: relative; overflow: hidden;
    box-shadow: 0 10px 30px rgba(0,0,0,.45);
  }

  /* Front: black side */
  .card--front {
    background: linear-gradient(135deg, #1c1c1c, var(--card-black) 60%, #0c0c0c);
    color: var(--grey-light);
  }
  .brand {
    position: absolute; left: 36px; top: 52px;
    display: flex; align-items: center; gap: 14px;
  }
  .brand__mark {
    width: 40px; height: 40px; background: var(--red);
  }
  .brand__name {
    font-family: "Cinzel", serif; font-weight: 700;
    font-size: 25px; line-height: 1.05; color: var(--red);
    letter-spacing: .5px;
  }
  .rule {
    position: absolute; height: 2px; background: var(--red);
  }
  .rule--main { left: 36px; right: 0; top: 142px; }
  .rule--name { left: 36px; width: 190px; top: 236px; }
  .contact {
    position: absolute; right: 28px; top: 160px;
    list-style: none;
    font-family: "Open Sans", sans-serif; font-size: 12.5px;
    color: #d6d6d6;
  }
  .contact__item {
    display: flex; align-items: center; justify-content: flex-end; gap: 9px;
    height: 22px;
  }
  .contact__icon {
    width: 15px; height: 15px; border-radius: 50%; background: var(--red);
    display: flex; align-items: center; justify-content: center; flex: none;
  }
  .person {
    position: absolute; left: 36px; top: 246px;
    font-family: "Cinzel", serif;
  }
  .person__name { font-size: 17px; font-weight: 700; color: #d0d0d0; }
  .person__name .first { color: var(--red); }
  .person__title { font-size: 14px; color: var(--grey-mid); margin-top: 2px; }

  /* Back: silver side */
  .card--back {
    background: linear-gradient(120deg, #6a6a6a 0%, #bdbdbd 25%, #f4f4f4 55%, #d2d2d2 75%, #8a8a8a 100%);
    display: flex; align-items: center; justify-content: center; gap: 16px;
  }
  .card--back .brand__mark { width: 52px; height: 52px; background: var(--grey-dark); }
  .card--back .brand__name { color: var(--grey-dark); font-size: 28px; }
</style>
</head>
<body>
<main class="stage">
  <section class="card card--front" aria-label="Card front">
    <div class="brand">
      <span class="brand__mark"></span>
      <span class="brand__name">The Harrowgate<br>Partners</span>
    </div>
    <div class="rule rule--main"></div>

    <ul class="contact">
      <li class="contact__item">www.theharrowgatepartners.example
        <span class="contact__icon">
          <svg width="9" height="9" viewBox="0 0 10 10" fill="none" stroke="#fff" stroke-width="1"><circle cx="5" cy="5" r="4"/><path d="M1 5h8M5 1c2 2 2 6 0 8M5 1c-2 2-2 6 0 8"/></svg>
        </span>
      </li>
      <li class="contact__item">(555)310-2968
        <span class="contact__icon">
          <svg width="8" height="9" viewBox="0 0 8 10"><rect x="1.5" y="0.5" width="5" height="9" rx="1" fill="none" stroke="#fff"/><circle cx="4" cy="8" r=".6" fill="#fff"/></svg>
        </span>
      </li>
      <li class="contact__item">Dana.Ostrander@theharrowgatepartners.example
        <span class="contact__icon">
          <svg width="9" height="7" viewBox="0 0 10 8" fill="none" stroke="#fff"><rect x=".5" y=".5" width="9" height="7"/><path d="M.5 .5 5 4.5 9.5 .5"/></svg>
        </span>
      </li>
    </ul>

    <div class="rule rule--name"></div>
    <div class="person">
      <p class="person__name"><span class="first">Dana</span> Ostrander</p>
      <p class="person__title">Principle</p>
    </div>
  </section>

  <section class="card card--back" aria-label="Card back">
    <span class="brand__mark"></span>
    <span class="brand__name">The Harrowgate<br>Partners</span>
  </section>
</main>
</body>
</html>
```